Design a Hemp Museum + exhibition design**

I'm creating an Online Museum for Hemp which will tell the story of hemp from ancient times to now and the future
cover the medical, industrial and nutritional uses and development of hemp
the people behind it, researchers, politicians, farmers and influencerts

the museum will have a number of "wings" , each holds an exhibition around a differnet theme, for example:

Hemp in the Age of Empires: 18th and 19th Century Collections
Hemp - The History of Healing
Domestication and Early Use: Ancient Collection
From Cotton Gin to Plastics and Prohibition: Hemp's Decline

these are just a few sample ideas for exhibitions

I'm looking for an overall design for the museum home page and exhibition page which will make people curious and want to spend time,learning and browsing

Think mobile -first :)

You are requested to design

1. Home page
2. Exhibition page

Target Market(s)

Hemp aficionados, curious fans

Logo Text

The Lumen Museum

Coding

Coded - Design and coding required

Number of Pages Required

3 page

Font styles to use
Sans Serif
Decorative

Requirements
Must have
• a homepage design which prompts visitors to immediately start watching an exhibition

visitors need to understand that this is a museum , so that they dont think it's a business, a service provider or anything like that

needs to have the usual links to T&C, privacy, about us

needs to have a link to "Wander past the lantern stall"

must have a visual WOW effect
Nice to have
• animations, sounds etc
Should not have
• forms like contact us etc - not relevant

```html
<!DOCTYPE html>
<html lang="en">
<head>
<meta charset="UTF-8">
<title>The Lumen Museum</title>
<link href="https://fonts.googleapis.com/css2?family=Poppins:wght@400;500;600;700&display=swap" rel="stylesheet">
<style>
:root{
  --ink:#0b0b0b;
  --smoke-dark:#161616;
  --smoke-mid:#3a3a3a;
  --white:#ffffff;
  --accent:#f7a21b;
  --leaf:#4f8f2a;
  --leaf-light:#8cc24e;
  --table:#5a5550;
  --muted:#cfcfcf;
}
*{margin:0;padding:0;box-sizing:border-box}
html,body{width:1200px;height:2359px;overflow:hidden;background:var(--ink)}
body{font-family:'Poppins',sans-serif;color:var(--white)}
.hero{position:relative;width:1200px;height:2359px;overflow:hidden;
  background:radial-gradient(ellipse 700px 500px at 600px 300px,var(--smoke-mid),transparent 70%),
             radial-gradient(ellipse 600px 700px at 200px 1200px,#2e2e2e,transparent 70%),
             linear-gradient(180deg,var(--smoke-dark) 0%,#242424 55%,#2b2a29 75%,var(--table) 100%);}
.scene-photo{position:absolute}
.plant-left{left:-40px;top:1560px;width:620px;height:620px;
  background:radial-gradient(ellipse at 50% 50%,var(--leaf-light) 0%,var(--leaf) 40%,rgba(60,110,30,.5) 62%,transparent 74%)}
.plant-right{left:640px;top:1160px;width:640px;height:940px;
  background:radial-gradient(ellipse at 55% 50%,var(--leaf-light) 0%,var(--leaf) 40%,rgba(60,110,30,.5) 62%,transparent 74%)}
.brand{position:absolute;left:38px;top:78px;font-size:62px;font-weight:700;color:var(--white);letter-spacing:-1px}
.menu-btn{position:absolute;left:1035px;top:52px;width:128px;height:128px;border-radius:50%;background:var(--white)}
.menu-btn span{position:absolute;right:34px;height:6px;border-radius:3px;background:var(--ink)}
.menu-btn span:nth-child(1){top:44px;width:52px}
.menu-btn span:nth-child(2){top:61px;width:62px}
.menu-btn span:nth-child(3){top:78px;width:44px}
.wing-index{position:absolute;left:36px;top:440px;list-style:none;font-weight:600;font-size:48px}
.wing-index li{position:absolute;left:0}
.wing-index .track{position:absolute;left:24px;top:90px;width:6px;height:200px;background:#777}
.intro{position:absolute;left:0;width:1245px;text-align:center}
.kicker{top:440px;font-size:70px;font-weight:500;letter-spacing:1px}
.title{top:535px;font-size:170px;font-weight:700;line-height:158px;letter-spacing:2px}
.title em{font-style:normal;color:var(--accent)}
.subtitle{top:895px;font-size:55px;font-weight:500;line-height:79px}
.cta{position:absolute;left:356px;top:1110px;width:533px;height:158px;background:var(--accent);
  display:flex;align-items:center;justify-content:center;font-size:62px;font-weight:700;letter-spacing:1px}
.wing-nav{position:absolute;left:165px;top:2100px;width:757px;height:259px;background:var(--ink);display:flex}
.wing-nav .item{width:50%;padding:45px 0 0 97px;position:relative}
.wing-nav .item + .item{padding-left:82px;border-left:3px solid #2c2c2c;margin-top:55px;padding-top:0}
.wing-nav .num{color:var(--accent);font-size:30px;font-weight:600}
.wing-nav .label{margin-top:40px;font-size:34px;font-weight:700}
.wing-nav .note{margin-top:4px;font-size:26px;color:var(--muted)}
.next-thumb{position:absolute;left:922px;top:2100px;width:278px;height:259px;
  background:radial-gradient(circle at 55% 45%,#6ea046,#3d6b26 55%,#d9d9d4 90%)}
</style>
</head>
<body>
<main class="hero">
  <div class="scene-photo plant-right" role="img" aria-label="Potted leafy plants on a table"></div>
  <div class="scene-photo plant-left" role="img" aria-label="Potted leafy plant in the foreground"></div>

  <header>
    <div class="brand">The Lumen Museum</div>
    <div class="menu-btn" aria-label="Menu"><span></span><span></span><span></span></div>
  </header>

  <ul class="wing-index">
    <li style="top:0">01</li>
    <li class="track"></li>
    <li style="top:320px">02</li>
    <li style="top:425px">03</li>
    <li style="top:530px">04</li>
    <li style="top:635px">05</li>
  </ul>

  <p class="intro kicker">THE WORLD’S ONLY</p>
  <h1 class="intro title">THE <em>LUMEN</em><br>MUSEUM</h1>
  <p class="intro subtitle">Hemp in the Age of Empires:<br>18th and 19th Century Collections</p>
  <a class="cta">OUR EXPLORE</a>

  <nav class="wing-nav">
    <div class="item">
      <div class="num">02</div>
      <div class="label">NEXT</div>
      <div class="note">No place to go</div>
    </div>
    <div class="item">
      <div class="num">03</div>
      <div class="label">COLLECTION</div>
      <div class="note">Nature peices</div>
    </div>
  </nav>
  <div class="next-thumb" role="img" aria-label="Preview of a leafy plant from the next collection"></div>
</main>
</body>
</html>
```